Lanternleaf - Fresh Asian Cuisine Menu

We need to redo our menu to include pictures of food items. Our restaurant is vibrant, trendy, upscale Chinese cuisine

Requirements
Must have
• Must fit on 8.5x11 paper. We can remove the About Us section if needed but menu cannot be more than 6 pages total. Must include pictures of menu items

```html
<!DOCTYPE html>
<html lang="en">
<head>
<meta charset="utf-8">
<title>Lanternleaf - Lunch Menu</title>
<link rel="stylesheet" href="https://fonts.googleapis.com/css2?family=Cinzel:wght@700&family=Great+Vibes&family=Signika:wght@500;600&family=Roboto+Condensed:wght@400&display=swap">
<style>
  :root {
    --backdrop: #8e1419;
    --paper: #ffffff;
    --paper-tint: #fbf6f6;
    --brand-red: #b3141c;
    --ink-red: #a3161d;
    --deep-red: #7e0f14;
    --photo-dark: #3a2420;
    --photo-warm: #c2502c;
    --photo-plate: #efe7e2;
    --ornament: #f3d6d7;
  }
  * { box-sizing: border-box; margin: 0; padding: 0; }
  html, body { width: 1200px; height: 1200px; overflow: hidden; }
  body { background: var(--backdrop); position: relative; }

  .menu-page {
    position: absolute; left: 150px; top: 18px;
    width: 900px; height: 1164px;
    background: linear-gradient(180deg, var(--paper) 0%, var(--paper-tint) 100%);
    color: var(--ink-red);
    font-family: "Roboto Condensed", sans-serif;
  }

  .corner-ornament { position: absolute; top: 9px; width: 102px; height: 77px; background: var(--ornament); border-radius: 4px; }
  .corner-ornament.left { left: 18px; }
  .corner-ornament.right { left: 776px; }

  .brand { position: absolute; left: 140px; top: 60px; display: flex; align-items: center; gap: 7px; }
  .brand-dot { width: 20px; height: 20px; border-radius: 50%; background: var(--brand-red); }
  .brand-name { font-family: "Signika", sans-serif; font-weight: 600; font-size: 18px; color: var(--brand-red); }

  .menu-title { position: absolute; left: 300px; top: 32px; font-family: "Cinzel", serif; font-weight: 700; font-size: 52px; color: var(--brand-red); letter-spacing: 1px; }
  .menu-hours { position: absolute; left: 307px; top: 90px; font-family: "Great Vibes", cursive; font-size: 22px; color: var(--ink-red); }

  .dish-name { font-family: "Signika", sans-serif; font-weight: 600; font-size: 20px; line-height: 22px; color: var(--ink-red); }
  .dish-desc { font-size: 12px; line-height: 15px; color: var(--ink-red); margin-top: 3px; }
  .dish-price { font-family: "Signika", sans-serif; font-weight: 500; font-size: 20px; color: var(--ink-red); }

  .photo-dish { position: absolute; display: flex; gap: 13px; }
  .photo-dish.left-col { left: 21px; width: 413px; }
  .photo-dish.right-col { left: 449px; width: 420px; }
  .dish-photo {
    flex: 0 0 121px; height: 81px; border: 1.5px solid var(--brand-red);
    background: radial-gradient(circle at 50% 50%, var(--photo-warm) 0 22%, var(--photo-plate) 24% 36%, var(--photo-dark) 40%);
  }
  .photo-dish .dish-info { padding-top: 9px; width: 235px; }
  .photo-dish .dish-price { position: absolute; right: 0; top: 7px; }

  .leader-dish { position: absolute; }
  .leader-dish.left-col { left: 56px; width: 378px; }
  .leader-dish.right-col { left: 467px; width: 402px; }
  .leader-row { display: flex; align-items: flex-end; gap: 8px; }
  .leader-dots { flex: 1; border-bottom: 2px dotted var(--ink-red); margin-bottom: 8px; }
  .leader-dish .dish-desc { width: 240px; }

  .footer-band { position: absolute; left: 0; right: 0; top: 1124px; height: 2px; background: var(--brand-red); }
  .footer-pattern { position: absolute; left: 0; right: 0; top: 1131px; height: 20px; background: var(--brand-red); }
</style>
</head>
<body>
<main class="menu-page">
  <div class="corner-ornament left" role="img" aria-label="Red lattice corner ornament with flower motif"></div>
  <div class="corner-ornament right" role="img" aria-label="Red lattice corner ornament with firework motif"></div>

  <div class="brand"><span class="brand-dot"></span><span class="brand-name">Lanternleaf</span></div>
  <h1 class="menu-title">LUNCH MENU</h1>
  <p class="menu-hours">available Monday – Friday from 11am to 3pm</p>

  <!-- Left column -->
  <article class="photo-dish left-col" style="top:144px">
    <div class="dish-photo" role="img" aria-label="Photo of Kung Pao Chicken"></div>
    <div class="dish-info"><h2 class="dish-name">Kung Pao Chicken</h2><p class="dish-desc">Chicken sautéed with roasted peanuts and dry red chili in Kung Pao sauce</p></div>
    <span class="dish-price">$10</span>
  </article>
  <article class="photo-dish left-col" style="top:233px">
    <div class="dish-photo" role="img" aria-label="Photo of Orange Chicken"></div>
    <div class="dish-info"><h2 class="dish-name">Orange Chicken</h2><p class="dish-desc">Battered-fried chicken breast with dried chili peppers and stir fried in a tangy orange flavored sauce</p></div>
    <span class="dish-price">$10</span>
  </article>
  <article class="photo-dish left-col" style="top:322px">
    <div class="dish-photo" role="img" aria-label="Photo of Crispy Spicy Chicken"></div>
    <div class="dish-info"><h2 class="dish-name">Crispy Spicy Chicken</h2><p class="dish-desc">Crispy-diced chicken with Sichuan peppers, garlic, scallions and red and green bell peppers</p></div>
    <span class="dish-price">$11</span>
  </article>
  <article class="photo-dish left-col" style="top:414px">
    <div class="dish-photo" role="img" aria-label="Photo of General Tso's Chicken"></div>
    <div class="dish-info"><h2 class="dish-name">General Tso’s Chicken</h2><p class="dish-desc">Battered-fried chicken breast, stir fried in a sweet &amp; tangy chili sauce with chili peppers</p></div>
    <span class="dish-price">$10</span>
  </article>
  <article class="photo-dish left-col" style="top:504px">
    <div class="dish-photo" role="img" aria-label="Photo of Shredded Chicken in Spicy Garlic Sauce"></div>
    <div class="dish-info" style="padding-top:0"><h2 class="dish-name">Shredded Chicken in Spicy Garlic Sauce</h2><p class="dish-desc">Battered-fried chicken breast with dried chili peppers and stir fried in a tangy orange flavored sauce</p></div>
    <span class="dish-price">$11</span>
  </article>
  <article class="photo-dish left-col" style="top:600px">
    <div class="dish-photo" role="img" aria-label="Photo of Sweet and Sour Chicken"></div>
    <div class="dish-info"><h2 class="dish-name">Sweet &amp; Sour Chicken</h2><p class="dish-desc">Crispy Chicken with green bell peppers, onions and pineapple glazed in a homemade sweet and sour marinade</p></div>
    <span class="dish-price">$10</span>
  </article>
  <article class="photo-dish left-col" style="top:701px">
    <div class="dish-photo" role="img" aria-label="Photo of Oyster Beef"></div>
    <div class="dish-info"><h2 class="dish-name">Oyster Beef</h2><p class="dish-desc">Tender cuts of steak wok fried with onions and marinated in a homemade oyster sauce</p></div>
    <span class="dish-price">$11</span>
  </article>
  <article class="photo-dish left-col" style="top:800px">
    <div class="dish-photo" role="img" aria-label="Photo of Dancing Pork Belly on rice cracker"></div>
    <div class="dish-info" style="padding-top:16px"><h2 class="dish-name">Dancing Pork Belly</h2><p class="dish-desc">Dancing Pork Belly Braised Pork Belly on sizzling rice cracker</p></div>
    <span class="dish-price" style="top:14px">$11</span>
  </article>

  <article class="leader-dish left-col" style="top:891px">
    <div class="leader-row"><h2 class="dish-name">Black Pepper Steak</h2><span class="leader-dots"></span><span class="dish-price">$12</span></div>
    <p class="dish-desc">Black Pepper Steak Tender cuts of steak mixed with onions and red and green bell peppers</p>
  </article>
  <article class="leader-dish left-col" style="top:979px">
    <div class="leader-row"><h2 class="dish-name">Twice Cooked Pork</h2><span class="leader-dots"></span><span class="dish-price">$11</span></div>
    <p class="dish-desc">Twice Cooked Pork Stir fried Pork Belly slices with leek and fermented black beans</p>
  </article>

  <!-- Right column -->
  <article class="leader-dish right-col" style="top:148px">
    <div class="leader-row"><h2 class="dish-name">Lemon Peel Shrimp</h2><span class="leader-dots"></span><span class="dish-price">$12</span></div>
    <p class="dish-desc">Shrimp with fresh lemons in a sweet lemon sauce on a bed of shredded lettuce</p>
  </article>
  <article class="leader-dish right-col" style="top:231px">
    <div class="leader-row"><h2 class="dish-name">Rice Wine Fish</h2><span class="leader-dots"></span><span class="dish-price">$11</span></div>
    <p class="dish-desc">White fish filet with rice wine mixed with onions, peas and carrots</p>
  </article>
  <article class="leader-dish right-col" style="top:321px">
    <div class="leader-row"><h2 class="dish-name">Lanternleaf Fried Rice</h2><span class="leader-dots"></span><span class="dish-price">$10</span></div>
    <p class="dish-desc">Shrimp, chicken, and beef, farm fresh eggs, onions, and scallions</p>
  </article>
  <article class="leader-dish right-col" style="top:412px">
    <div class="leader-row"><h2 class="dish-name">Vegetarian White<br>Fried Rice</h2><span class="leader-dots" style="margin-bottom:30px"></span><span class="dish-price" style="margin-bottom:22px">$9</span></div>
    <p class="dish-desc">Mixed vegetables with white rice</p>
  </article>
  <article class="leader-dish right-col" style="top:506px">
    <div class="leader-row"><h2 class="dish-name">Lanternleaf Lo Mein</h2><span class="leader-dots"></span><span class="dish-price">$10</span></div>
    <p class="dish-desc">Shrimp, chicken, and beef, farm fresh eggs, onions, and scallions</p>
  </article>
  <article class="leader-dish right-col" style="top:593px">
    <div class="leader-row"><h2 class="dish-name">Vegetarian Lo Mein</h2><span class="leader-dots"></span><span class="dish-price">$9</span></div>
    <p class="dish-desc">Mixed vegetables with lo mein noodles</p>
  </article>

  <article class="photo-dish right-col" style="top:670px">
    <div class="dish-photo" role="img" aria-label="Photo of Mapo Tofu"></div>
    <div class="dish-info"><h2 class="dish-name">Mapo Tofu</h2><p class="dish-desc">Battered-fried chicken breast with dried chili peppers and stir fried in a tangy orange flavored sauce</p></div>
    <span class="dish-price">$9</span>
  </article>
  <article class="photo-dish right-col" style="top:770px">
    <div class="dish-photo" role="img" aria-label="Photo of Spicy Garlic Eggplant"></div>
    <div class="dish-info"><h2 class="dish-name">Spicy Garlic Eggplant</h2><p class="dish-desc">Chinese eggplant in spicy garlic sauce garnished with scallions</p></div>
    <span class="dish-price" style="top:12px">$10</span>
  </article>
  <article class="photo-dish right-col" style="top:859px">
    <div class="dish-photo" role="img" aria-label="Photo of Stir Fried Eggplant"></div>
    <div class="dish-info"><h2 class="dish-name">Stir Fried Eggplant</h2><p class="dish-desc">Chinese eggplant with sautéed green beans</p></div>
    <span class="dish-price" style="top:12px">$10</span>
  </article>
  <article class="photo-dish right-col" style="top:961px">
    <div class="dish-photo" role="img" aria-label="Photo of Shiitake Baby Bok Choy"></div>
    <div class="dish-info"><h2 class="dish-name">Shiitake Baby Bok</h2><p class="dish-desc">Sautéed baby bok-choy with Shiitake mushrooms in brown sauce</p></div>
    <span class="dish-price" style="top:12px">$10</span>
  </article>

  <div class="footer-band"></div>
  <div class="footer-pattern" role="img" aria-label="Red Chinese key fret border pattern"></div>
</main>
</body>
</html>
```